Construction company featuring multiple photos to highlight work. Looking for clean modern design.

-Clean and modern design ****(SEE THUMBNAIL FILES FOR EASY PROJECT GROUPINGS)
-Looking for photos to be highlighted in a unique way to show before and after photos of Construction projects. (Please refer to this website for a possible layout . This is NOT our company but we like the layout of photos www.plovanstudio.com We dont want to copy any website but wanted to guide designers in the right direction.
will be uploading more content but looking for photo layout as a big part of the website design
******VERY IMPORTANT. Please see the 5 file uploads called THUMBNAILS for help with photo groups. this is to help you see the groups of photos that need to go together. (I have then uploaded the individual photos separately from thumbnail for better quality photos.)
****The photos that have been uploaded are labeled by room and house number(For example 3106 is a house number then it will say before or progress or after to show the project. . we would prefer to highlight projects by bathroom remodel, kitchen remodel, wood flooring and trim package jobs etc. NOT by house number. the house number was only to organize the photos not to list them on website by house number.
++++ Would like it to be very clear that the before photos are before construction begins.
++++Was maybe picturing small icons to show the before photos and a Larger slideshow showing the completed designs.
++++Feature photos would be the 3106 photos Kitchen/family room , bathrooms labeled 3106 is most current work.
++++Some photo catagories could be ....
-Kitchens Photos
-Bathrooms Photos
-Flooring/Doors/Trim Photos
-New Construction/Real Estate Renovations Photos
-Home Additions Photos
-Insurance Claims Fire and Water Damage Photos
-----Our Services:
-Remodeling Kitchen & Bath
-Insurance Claims Fire and Water Damage Repairs
-Home Additions / New Home Construction
-Flooring, tile, decking
-Custom built-ins and trim/door remodel
-Interior & Exterior Painting
-Roofing

Contact Us information:
Ashmoor Construction (Charleston South Carolina)
827 Tarrow Lane
Suite 415
Mount Pleasant, SC 29471
Owner: Dennis Roulard
Phone (803) 555-0147
Email: droulard@ashmoorbuild.com
Ashmoor Construction Website Content
-----Bio: Dennis Roulard, owner of Ashmoor Construction has over 17 years of experience working with customers on remodeling, renovation projects, and insurance related fire and water damage repairs.
----Contact us today to set up a free consultation.
(803) 555-0147
Will upload more text content soon

Industry/Entity Type

Residential General Contractor

Coding

Coded - Design and coding required

Requirements
Must have
• Ashmoor Construction Website Content Bio: Dennis Roulard, owner of Ashmoor Construction has over 17 years of experience working with customers on remodeling, renovation projects, and insurance related fire and water damage repairs. Contact us today to set up a free consultation. (803) 555-0147
Nice to have
• Nice to have a contact us page that can have a call now button with phone number or email. Would be really great if there could a way to have reviews populate from Verlo reviews.

```html
<!DOCTYPE html>
<html lang="en">
<head>
<meta charset="utf-8">
<title>Ashmoor Construction</title>
<link rel="stylesheet" href="https://fonts.googleapis.com/css2?family=Michroma&family=Roboto:wght@400;500;700&display=swap">
<style>
:root{
  --blue:#86a3d1;
  --blue-band:#9bb4db;
  --ink:#1d1d1f;
  --body:#6a6a6a;
  --dark:#2b2b2d;
  --white:#ffffff;
  --black:#000000;
  --star:#f4b400;
}
*{margin:0;padding:0;box-sizing:border-box}
html,body{width:1200px;height:4505px;overflow:hidden;background:var(--white)}
body{position:relative;font-family:'Roboto',Arial,sans-serif;color:var(--ink)}
.abs{position:absolute}
.display{font-family:'Michroma',Arial,sans-serif;text-transform:uppercase;letter-spacing:1px}
.btn{position:absolute;background:var(--blue);color:var(--white);font-size:15px;font-weight:500;display:flex;align-items:center;justify-content:center;border-radius:3px}
.photo{position:absolute}
.wordmark{position:absolute;display:flex;flex-direction:column;align-items:center;color:var(--white);font-family:'Michroma',Arial,sans-serif;text-transform:uppercase}
.wordmark .mark{width:22px;height:22px;background:var(--white);margin-bottom:10px}
.wordmark .name{font-size:34px;letter-spacing:3px;line-height:1}
.wordmark .sub{font-size:13px;letter-spacing:4px;margin-top:8px}

/* hero */
.hero-photo{left:0;top:0;width:1200px;height:607px;background:linear-gradient(180deg,#b7c7d8 0%,#8a8f86 45%,#c9c3b8 100%)}
.hero-panel{left:157px;top:65px;width:887px;height:475px;background:rgba(40,40,42,.88)}
.menu{left:992px;top:96px;width:22px;height:18px}
.hero-title{left:157px;top:286px;width:887px;text-align:center;color:var(--white);font-size:44px;line-height:50px}

/* about */
.about-title{left:112px;top:706px;font-size:40px}
.about-text{left:112px;top:768px;width:365px;font-size:14px;line-height:28px;color:var(--body)}
.about-photo{left:519px;top:696px;width:569px;height:451px;background:linear-gradient(135deg,#d0d0d0,#6e6e6e);box-shadow:0 4px 16px rgba(0,0,0,.18)}
.quote-card{left:112px;top:960px;width:574px;height:163px;background:var(--white);box-shadow:0 4px 18px rgba(0,0,0,.14);border-bottom:4px solid var(--blue);padding:26px 26px}
.quote-card p{font-size:14px;line-height:27px;color:var(--body)}
.quote-card .who{margin-top:6px;color:var(--blue);font-weight:700;font-size:17px}

/* categories */
.cat-band{left:0;top:1263px;width:1200px;height:572px;background:linear-gradient(180deg,#2e2e30,#3c3c3e)}
.cat-title{left:0;top:1356px;width:1200px;text-align:center;color:var(--white);font-size:40px}
.cat{position:absolute;width:232px;height:140px;background:var(--white);border-radius:3px;display:flex;flex-direction:column;align-items:center;justify-content:center;font-size:15px;color:#555}
.cat svg{width:46px;height:46px;margin-bottom:14px;fill:none;stroke:#666;stroke-width:1.6}
.cat.go{background:var(--blue);color:var(--white);font-weight:500;font-size:16px}
.cat.go svg{width:30px;height:30px;stroke:none}

/* services */
.sec-title{left:0;width:1200px;text-align:center;font-size:40px}
.svc-card{left:112px;top:2006px;width:976px;height:492px;background:var(--white);box-shadow:0 3px 16px rgba(0,0,0,.13)}
.svc-photo{left:128px;top:2022px;width:470px;height:460px;background:linear-gradient(180deg,#e7e8e6,#9a8c7c)}
.svc-head{left:649px;top:2064px;width:380px;font-size:27px;line-height:37px}
.svc-text{left:649px;top:2148px;width:372px;font-size:12px;line-height:23px;color:var(--body)}
.arrow{position:absolute;width:32px;height:32px;border-radius:50%;display:flex;align-items:center;justify-content:center}
.arrow.soft{background:#cfcfcf}
.arrow.strong{background:#3a3a3c}
.arrow svg{width:14px;height:14px;stroke:var(--white);stroke-width:2.5;fill:none}

/* bands */
.band{left:0;width:1200px;height:123px;background:var(--blue-band);display:flex;align-items:center;justify-content:center;color:var(--white);font-size:40px}

/* portfolio */
.pf-before{left:129px;top:2797px;width:471px;height:426px;background:linear-gradient(160deg,#d9d2c0,#3e4d7c)}
.pf-after{left:600px;top:2797px;width:470px;height:426px;background:linear-gradient(160deg,#f3f2ee,#b59a7a)}
.pf-divider{left:598px;top:2797px;width:3px;height:426px;background:var(--white)}
.pf-handle{left:572px;top:2994px;width:56px;height:32px;background:rgba(255,255,255,.9);display:flex;justify-content:space-around;align-items:center;border-radius:3px}
.pf-handle svg{width:12px;height:12px;stroke:#555;stroke-width:2;fill:none}

/* reviews */
.review{position:absolute;top:3585px;width:467px;height:245px;background:var(--white);box-shadow:0 3px 16px rgba(0,0,0,.12);padding:30px 34px}
.review .q{font-family:Georgia,serif;font-size:54px;line-height:40px;color:var(--blue);font-weight:700}
.review p{font-size:12px;line-height:24px;color:var(--body);margin-top:6px}
.review .by{display:flex;align-items:center;margin-top:12px}
.review .dot{width:30px;height:30px;border-radius:50%;border:4px solid #9aa5b8;margin-right:16px}
.review .stars{color:var(--star);font-size:13px;letter-spacing:1px}
.review .name{font-size:12px;font-weight:700;color:var(--ink)}

/* footer */
.footer{left:0;top:4072px;width:1200px;height:433px;background:var(--black)}
.cta{left:86px;top:3993px;width:1028px;height:161px;background:var(--blue);border-radius:4px;color:var(--white)}
.cta-text{left:34px;top:40px;font-size:28px;line-height:43px}
.cta-phone{right:34px;top:56px;font-size:40px;font-weight:700;letter-spacing:1px}
.nav{left:0;top:4347px;width:1200px;display:flex;justify-content:center;color:var(--white);font-size:15px}
.nav span{padding:0 44px}
.nav i{font-style:normal;color:#aaa}
.social{left:0;top:4398px;width:1200px;display:flex;justify-content:center;gap:16px}
.social span{width:30px;height:30px;border-radius:50%;background:var(--white)}
.copy{left:0;top:4450px;width:1200px;text-align:center;color:var(--white);font-size:13px}
</style>
</head>
<body>

<!-- hero -->
<div class="abs hero-photo" role="img" aria-label="White two-storey house with palm trees and a curved staircase"></div>
<div class="abs hero-panel"></div>
<svg class="abs menu" viewBox="0 0 22 18"><path d="M2 2h20M8 9h14M2 16h20" stroke="#fff" stroke-width="2"/></svg>
<div class="wordmark" style="left:440px;top:142px;width:320px">
  <span class="mark"></span>
  <span class="name">Ashmoor</span>
  <span class="sub">Construction</span>
</div>
<h1 class="abs display hero-title">Welcome to Ashmoor<br>Construction</h1>
<div class="btn" style="left:518px;top:411px;width:162px;height:49px">View Portfolio</div>

<!-- about -->
<h2 class="abs display about-title">About Me</h2>
<p class="abs about-text">For more than a decade we have helped local families plan, build and finish the rooms they live in every day. Every project starts with a clear walkthrough, an honest estimate, and a crew that treats your home as if it were.</p>
<div class="abs about-photo" role="img" aria-label="Black and white family portrait of the owner with his wife and two children"></div>
<div class="abs quote-card">
  <p>Owner of Ashmoor Construction has over 17 years of experience working with customers on remodeling, renovation projects, and insurance related fire and water damage repairs.</p>
  <div class="who">Dennis Roulard</div>
</div>

<!-- categories -->
<div class="abs cat-band" role="img" aria-label="Darkened photo of a finished kitchen interior"></div>
<h2 class="abs display cat-title">Our Catagories</h2>
<div class="cat" style="left:112px;top:1439px"><svg viewBox="0 0 46 46"><rect x="6" y="22" width="34" height="18"/><path d="M6 30h34M23 22v18M10 8h12v9H10zM28 8h10v9H28z"/></svg>Kitchens</div>
<div class="cat" style="left:359px;top:1439px"><svg viewBox="0 0 46 46"><rect x="6" y="6" width="18" height="16"/><path d="M6 26h22v4a10 10 0 0 1-22 0zM32 20h8v10a4 4 0 0 1-8 0z"/></svg>Bathrooms</div>
<div class="cat" style="left:607px;top:1439px"><svg viewBox="0 0 46 46"><rect x="8" y="6" width="30" height="34"/><path d="M23 6v34M12 26l8-8M26 26l8-8"/></svg>Flooring/Doors/Trim</div>
<div class="cat" style="left:855px;top:1439px"><svg viewBox="0 0 46 46"><path d="M4 22L23 6l19 16M9 18v22h28V18M17 40V28h12v12"/></svg>Real Estate Renovations</div>
<div class="cat" style="left:112px;top:1595px"><svg viewBox="0 0 46 46"><path d="M4 22L23 6l19 16M9 18v22h28V18M23 24v10M18 29h10"/></svg>Home Additions</div>
<div class="cat" style="left:359px;top:1595px"><svg viewBox="0 0 46 46"><path d="M4 24L20 10l16 14M8 20v20h24V20M14 40V30h8v10M34 6c4 4 4 8 0 10c-4-2-4-6 0-10z"/></svg>Insurance Claims Fire</div>
<div class="cat" style="left:607px;top:1595px"><svg viewBox="0 0 46 46"><path d="M6 24L22 10l16 14M10 20v20h20V20M32 26c4 5 5 8 2 10s-6 0-5-4z"/></svg>Water Damage</div>
<div class="cat go" style="left:855px;top:1595px"><svg viewBox="0 0 30 30"><circle cx="15" cy="15" r="13" fill="#fff"/><path d="M13 9l6 6-6 6" stroke="#86a3d1" stroke-width="2.5" fill="none"/></svg>Get Started Now</div>

<!-- services -->
<h2 class="abs display sec-title" style="top:1908px">Our Services</h2>
<div class="abs svc-card"></div>
<div class="abs svc-photo" role="img" aria-label="Remodeled dining nook with pendant lights and a wooden table"></div>
<h3 class="abs display svc-head">Remodeling Kitchen &amp; Bath</h3>
<p class="abs svc-text">From layout and cabinetry to tile, lighting and fixtures, we handle every stage of a kitchen or bathroom remodel. We plan the work around your schedule, keep the site clean, and walk you through each step so there are no surprises. Our crews finish trim, paint and hardware with care, and we stay in touch until the final walkthrough is signed off and the room is ready to use every day.</p>
<div class="btn" style="left:649px;top:2382px;width:163px;height:49px">View Portfolio</div>
<div class="arrow soft" style="left:42px;top:2237px"><svg viewBox="0 0 14 14"><path d="M9 2L4 7l5 5"/></svg></div>
<div class="arrow strong" style="left:1125px;top:2237px"><svg viewBox="0 0 14 14"><path d="M5 2l5 5-5 5"/></svg></div>

<!-- portfolio -->
<div class="abs band display" style="top:2599px" role="img" aria-label="Faded photo of a house under construction">Our Portfolio</div>
<div class="abs pf-before" role="img" aria-label="Living room before renovation"></div>
<div class="abs pf-after" role="img" aria-label="Finished open kitchen and dining area after renovation"></div>
<div class="abs pf-divider"></div>
<div class="abs pf-handle"><svg viewBox="0 0 12 12"><path d="M8 1L3 6l5 5"/></svg><svg viewBox="0 0 12 12"><path d="M4 1l5 5-5 5"/></svg></div>
<div class="arrow soft" style="left:42px;top:2994px"><svg viewBox="0 0 14 14"><path d="M9 2L4 7l5 5"/></svg></div>
<div class="arrow strong" style="left:1125px;top:2994px"><svg viewBox="0 0 14 14"><path d="M5 2l5 5-5 5"/></svg></div>
<div class="btn" style="left:518px;top:3265px;width:164px;height:49px">View Portfolio</div>

<!-- reviews -->
<div class="abs band display" style="top:3386px" role="img" aria-label="Faded photo of house framing">Happy Customers</div>
<div class="review" style="left:114px">
  <div class="q">&ldquo;</div>
  <p>The crew arrived on time every day and kept us informed from start to finish. Our new kitchen looks better than we imagined, and the work was done well.</p>
  <div class="by"><span class="dot"></span><div><div class="stars">★★★★★</div><div class="name">Liam Porter</div></div></div>
</div>
<div class="review" style="left:619px">
  <div class="q">&ldquo;</div>
  <p>The crew arrived on time every day and kept us informed from start to finish. Our new kitchen looks better than we imagined, and the work was done well.</p>
  <div class="by"><span class="dot"></span><div><div class="stars">★★★★★</div><div class="name">Liam Porter</div></div></div>
</div>
<div class="btn" style="left:518px;top:3867px;width:164px;height:49px">View More</div>

<!-- footer -->
<div class="abs footer"></div>
<div class="abs cta">
  <div class="abs display cta-text">Contact us today to set up<br>a free consultation</div>
  <div class="abs cta-phone">(803) 555-0147</div>
</div>
<div class="wordmark" style="left:440px;top:4196px;width:320px">
  <span class="mark"></span>
  <span class="name">Ashmoor</span>
  <span class="sub">Construction</span>
</div>
<nav class="abs nav"><span>Home</span><i>|</i><span>About Us</span><i>|</i><span>Services</span><i>|</i><span>Portfolio</span><i>|</i><span>Reviews</span><i>|</i><span>Contact Us</span></nav>
<div class="abs social"><span></span><span></span><span></span></div>
<div class="abs copy">© Copyright 2023 Ashmoor Construction | All Rights Reserved.</div>

</body>
</html>
```